Business Card Design

We have recently seen two business cards that caught our attention and think the designs would work for us. We are an accounting firm that serves small businesses in a variety of industries. Attached are the two business card that inspired us along with very rough layouts. We would like to see a professional layout using our company information.

Industry/Entity Type

Accounting

Contact Information for Business Card

Company Name - Porter Lyle
Address - 4120 Marbury Lane, Suite 310, Houston, TX 77058
713-555-0186 - Main
281-555-0143 - Fax

Team Member Names, emails and phone numbers (see attachment)

```html
<!DOCTYPE html>
<html lang="en">
<head>
<meta charset="utf-8">
<title>Porter Lyle Business Card</title>
<link href="https://fonts.googleapis.com/css2?family=Didact+Gothic&family=Merriweather:wght@700&display=swap" rel="stylesheet">
<style>
  :root {
    --backdrop: #ebe8df;
    --panel-grey: #e4e4e4;
    --card-white: #fafafa;
    --ink: #1a1a1a;
    --ink-soft: #555555;
    --card-black: #000000;
    --reverse-text: #d9d9d9;
    --mark-grey: #9a9a9a;
  }
  * { margin: 0; padding: 0; box-sizing: border-box; }
  html, body {
    width: 1200px;
    height: 1000px;
    overflow: hidden;
    background: var(--backdrop);
  }
  .canvas {
    position: relative;
    width: 1200px;
    height: 1000px;
  }
  .card {
    position: absolute;
    top: 348px;
    width: 540px;
    height: 304px;
    box-shadow: 0 3px 10px rgba(0,0,0,0.18);
    overflow: hidden;
  }
  /* Front */
  .card-front {
    left: 40px;
    display: flex;
    background: var(--card-white);
  }
  .brand-panel {
    position: relative;
    width: 250px;
    height: 100%;
    background: var(--panel-grey);
    display: flex;
    flex-direction: column;
    align-items: center;
    justify-content: center;
    gap: 16px;
  }
  .brand-panel::after {
    content: "";
    position: absolute;
    top: 0;
    right: -14px;
    width: 14px;
    height: 100%;
    background: linear-gradient(to right, rgba(0,0,0,0.16), rgba(0,0,0,0));
  }
  .brand-square {
    width: 58px;
    height: 58px;
    background: var(--ink);
  }
  .brand-name {
    font-family: "Merriweather", serif;
    font-weight: 700;
    font-size: 20px;
    letter-spacing: 0.06em;
    color: var(--ink);
  }
  .contact-panel {
    padding: 38px 0 0 22px;
    font-family: "Didact Gothic", sans-serif;
    color: var(--ink-soft);
    font-size: 17px;
    line-height: 1.22;
  }
  .contact-name { color: var(--ink); font-size: 18px; }
  .contact-block { margin-top: 20px; }
  .contact-email { margin-top: 20px; }
  /* Back */
  .card-back {
    left: 620px;
    background: var(--card-black);
  }
  .back-brand {
    position: absolute;
    right: 36px;
    bottom: 42px;
    text-align: right;
    font-family: "Didact Gothic", sans-serif;
  }
  .back-mark {
    display: flex;
    align-items: center;
    justify-content: flex-end;
    gap: 10px;
    font-size: 22px;
    letter-spacing: 0.08em;
    color: var(--reverse-text);
  }
  .back-square {
    width: 22px;
    height: 22px;
    background: var(--mark-grey);
  }
  .back-url {
    margin-top: 22px;
    font-size: 20px;
    color: var(--reverse-text);
  }
</style>
</head>
<body>
<main class="canvas">
  <section class="card card-front">
    <div class="brand-panel">
      <div class="brand-square"></div>
      <div class="brand-name">PORTER LYLE</div>
    </div>
    <div class="contact-panel">
      <div class="contact-name">Maren Holt</div>
      <div>Account Manager</div>
      <div class="contact-block">
        4120 Marbury Lane, Suite 310<br>
        Houston, TX 77058
      </div>
      <div class="contact-block">
        Office 713-555-0186<br>
        Direct 713-555-0172<br>
        Mobile 832-555-0119
      </div>
      <div class="contact-email">mholt@porterlyle.com</div>
    </div>
  </section>

  <section class="card card-back">
    <div class="back-brand">
      <div class="back-mark"><span class="back-square"></span>PORTER LYLE</div>
      <div class="back-url">porterlyle.com</div>
    </div>
  </section>
</main>
</body>
</html>
```